VMR business card

Need a business card for a company that provides instructional design and elearning development services. The website is here: http://vantmoro.studio/

I'm attaching a current logo, as well as the old business card design. While I like to keep it clean, the old design is too simplistic for my liking. The only idea I want to reuse from the old design is placing industry jargon on the back of the card, just need a better way to present it. But if you have other ideas for the back--feel free to experiment.

Please use the colors complementary to the color we have on the website. Thank you!

```html
<!DOCTYPE html>
<html lang="en">
<head>
<meta charset="utf-8">
<title>VMR business card</title>
<link rel="stylesheet" href="https://fonts.googleapis.com/css2?family=Open+Sans:wght@400;600;700&display=swap">
<style>
  :root {
    --page-bg: #e9e7e2;
    --card-white: #ffffff;
    --sand: #dccd8f;
    --teal: #17b1ab;
    --ink: #1c1c1c;
    --brand-ink: #2a9f9a;
  }
  html, body {
    margin: 0;
    width: 1200px;
    height: 900px;
    overflow: hidden;
    background: var(--page-bg);
  }
  .stage {
    width: 1200px;
    height: 900px;
    display: flex;
    align-items: center;
    justify-content: center;
  }
  .business-card {
    width: 900px;
    height: 556px;
    box-shadow: 0 10px 30px rgba(0,0,0,0.18);
    background: var(--card-white);
  }
  .business-card svg { display: block; width: 100%; height: 100%; }
  .wave-teal { fill: var(--teal); }
  .wave-gap { fill: var(--card-white); }
  .wave-sand { fill: var(--sand); }
  .brand-name {
    font-family: "Open Sans", sans-serif;
    font-weight: 600;
    font-size: 34px;
    fill: var(--brand-ink);
  }
  .holder-name {
    font-family: "Open Sans", sans-serif;
    font-weight: 700;
    font-size: 21px;
    fill: var(--ink);
  }
  .contact-line {
    font-family: "Open Sans", sans-serif;
    font-weight: 400;
    font-size: 16px;
    fill: var(--ink);
  }
  .contact-icon { fill: var(--ink); }
</style>
</head>
<body>
<main class="stage">
  <section class="business-card" aria-label="VMR business card front">
    <svg viewBox="0 0 652 403" xmlns="http://www.w3.org/2000/svg">
      <rect width="652" height="403" fill="var(--card-white)"/>

      <g class="card-wave">
        <path class="wave-teal" d="M0,232 C60,290 120,320 200,312 C320,300 420,146 540,150 C600,152 635,170 652,186 L652,403 L0,403 Z"/>
        <path class="wave-gap" d="M0,244 C60,302 120,332 200,324 C320,312 420,160 540,164 C600,166 635,184 652,200 L652,403 L0,403 Z"/>
        <path class="wave-sand" d="M0,252 C60,308 120,338 200,330 C320,318 420,170 540,174 C600,176 635,192 652,208 L652,403 L0,403 Z"/>
      </g>

      <text class="brand-name" x="48" y="238">Vantmoro Studio</text>

      <text class="holder-name" x="617" y="268" text-anchor="end">Daniel Marsh</text>

      <g class="contact-list">
        <text class="contact-line" x="592" y="320" text-anchor="end">555-014-2287</text>
        <path class="contact-icon" d="M603,310 q2,-2 4,0 l2,3 q1,1.5 -0.5,2.5 q1,3 4,4.5 q1,-1.5 2.5,-0.5 l3,2 q1.5,2 -0.5,4 q-4,2 -9,-3 q-6,-6 -5.5,-12.5 z"/>

        <text class="contact-line" x="592" y="343" text-anchor="end">dmarsh@vantmoro.studio</text>
        <rect class="contact-icon" x="603" y="334" width="12" height="9" rx="1"/>
        <path d="M603.5,335 L609,339.5 L614.5,335" fill="none" stroke="var(--sand)" stroke-width="1.2"/>

        <text class="contact-line" x="592" y="366" text-anchor="end">www.vantmoro.studio</text>
        <circle class="contact-icon" cx="609" cy="361" r="6"/>
        <path d="M603.5,361 h11 M609,355.2 q-3.5,5.8 0,11.6 M609,355.2 q3.5,5.8 0,11.6" fill="none" stroke="var(--sand)" stroke-width="1"/>
      </g>
    </svg>
  </section>
</main>
</body>
</html>
```